Gardener needs an exciting new flyer design.

I'm a passionate gardener that requires a custom flyer design for a owner operator gardening business. Design will be for a DL flyer. I'm based on the Sunshine coast in Queensland Australia. My target audience is the residential market on the Sunshine coast. Business name is Marlowe Greens. My services are, lawn mowing, weeding, Eco Friendly fertilizing, green waste removal, Mulching, tree and shrub pruning, Full garden makeovers, hedging, pressure cleaning, privacy screening, Timber deck rejuvenation, Planting, Turf preparation and installation, and much more. Free no obligation quotes, reliable and friendly service, great rates. 12 years experience. Web www.marlowegreens.com.au - Phone 0418527064 - Email doug@marlowegreens.com.au I would like the design to portray a friendly and professional approach.

Target Market(s)

Residential

Industry/Entity Type

Gardener

Font styles to use
Serif

Colors
9ccb3b
abd037
3176b5

Requirements
Must have
• my services, my logo, my contact details,

```html
<!DOCTYPE html>
<html lang="en">
<head>
<meta charset="utf-8">
<title>Marlowe Greens DL Flyer</title>
<link href="https://fonts.googleapis.com/css2?family=Lato:wght@400;700&family=Montserrat:wght@400;500;600;800&display=swap" rel="stylesheet">
<style>
  :root {
    --page-bg: #d9d9d9;
    --paper: #ffffff;
    --green: #38994a;
    --green-dark: #2d7d3b;
    --purple: #4b1d57;
    --ink: #3d3d3d;
    --white: #ffffff;
    --photo-dark: #2f4a26;
    --photo-mid: #5d7a3e;
    --photo-deck: #8a7565;
    --portrait-a: #c99a7a;
    --portrait-b: #7a5a44;
  }
  * { margin: 0; padding: 0; box-sizing: border-box; }
  html, body {
    width: 800px; height: 1200px; overflow: hidden;
    background: var(--page-bg);
  }
  .canvas { position: relative; width: 800px; height: 1200px; }
  .flyer {
    position: absolute; left: 111px; top: 5px;
    width: 556px; height: 1143px;
    background: var(--paper);
    transform: scale(1.04); transform-origin: top left;
    overflow: hidden;
    font-family: "Lato", sans-serif;
    color: var(--ink);
  }
  .flyer-shapes { position: absolute; left: 0; top: 0; }
  .headline {
    position: absolute; left: 46px; top: 188px;
    font-family: "Montserrat", sans-serif; font-weight: 800;
    color: var(--white); line-height: 1;
    text-shadow: 0 0 2px #111, 1px 1px 2px #111, -1px -1px 2px #111;
  }
  .headline .kicker { display: block; font-size: 29px; }
  .headline .hero { display: block; font-size: 63px; letter-spacing: 1px; margin-top: 2px; }
  .headline .tail { display: block; font-size: 25px; margin-top: 4px; }
  .portrait {
    position: absolute; left: 353px; top: 429px;
    width: 130px; height: 130px; border-radius: 50%;
    border: 4px solid var(--white);
    background: radial-gradient(circle at 50% 45%, var(--portrait-a), var(--portrait-b));
    box-shadow: 0 2px 6px rgba(0,0,0,.35);
  }
  .promo {
    position: absolute; left: 40px; top: 590px; width: 262px;
    color: var(--white); font-family: "Montserrat", sans-serif;
  }
  .promo .line { display: block; font-size: 19px; line-height: 22px; font-weight: 400; }
  .promo .line.strong { font-weight: 500; }
  .promo .call { margin-top: 8px; }
  .promo .phone { display: block; font-size: 27px; font-weight: 500; margin-top: 2px; }
  .welcome { position: absolute; left: 43px; top: 716px; width: 262px; color: var(--white); }
  .welcome h2 {
    font-family: "Montserrat", sans-serif; font-weight: 600;
    font-size: 18px; line-height: 23px; margin-bottom: 10px;
  }
  .welcome p { font-size: 12.4px; line-height: 16px; margin-bottom: 12px; }
  .profile { position: absolute; left: 330px; top: 580px; width: 215px; }
  .profile h3, .services h3 {
    font-family: "Lato", sans-serif; font-weight: 700;
    color: var(--purple); font-size: 17px; line-height: 20px;
  }
  .profile p { font-size: 12px; line-height: 16px; margin-top: 2px; }
  .services { position: absolute; left: 328px; width: 222px; }
  .services.core { top: 694px; }
  .services.extra { top: 868px; }
  .services ul { list-style: none; margin-top: 2px; }
  .services li {
    position: relative; padding-left: 16px;
    font-size: 12.3px; line-height: 15px;
  }
  .services li::before {
    content: ""; position: absolute; left: 2px; top: 5px;
    width: 5px; height: 5px; border-radius: 50%; background: var(--green);
  }
  .footer { position: absolute; left: 0; top: 1008px; width: 556px; height: 135px; }
  .brand {
    position: absolute; left: 30px; top: 56px; width: 170px;
    display: flex; align-items: center; justify-content: center; gap: 7px;
    color: var(--green-dark); font-weight: 700; font-size: 17px;
  }
  .brand .dot { width: 12px; height: 12px; border-radius: 50%; background: var(--green); }
  .divider {
    position: absolute; left: 203px; top: 24px; width: 1px; height: 84px;
    background: #b9b9b9;
  }
  .contact { position: absolute; left: 223px; top: 26px; font-size: 9.5px; letter-spacing: .6px; color: #222; }
  .contact h3 {
    font-family: "Lato", sans-serif; font-weight: 700;
    color: var(--green); font-size: 16px; letter-spacing: 0; margin-bottom: 9px;
  }
  .contact .row { display: flex; align-items: center; gap: 6px; }
  .contact .row.bottom { margin-top: 10px; gap: 24px; }
  .contact .pair { display: flex; align-items: center; gap: 6px; }
  .contact .web-lines { line-height: 13px; }
</style>
</head>
<body>
<div class="canvas">
  <article class="flyer">
    <svg class="flyer-shapes" width="556" height="1008" viewBox="0 0 556 1008">
      <defs>
        <linearGradient id="gardenPhoto" x1="0" y1="0" x2="0" y2="1">
          <stop offset="0" stop-color="var(--photo-dark)"/>
          <stop offset="0.55" stop-color="var(--photo-mid)"/>
          <stop offset="0.75" stop-color="var(--photo-deck)"/>
          <stop offset="1" stop-color="#6f5e52"/>
        </linearGradient>
      </defs>
      <polygon points="0,0 556,0 556,465 0,565" fill="url(#gardenPhoto)"
        role="img" aria-label="Photo of a garden deck with a hanging wicker egg chair, potted flowers and pink oleander among trees"/>
      <polygon points="0,565 312,509 312,1008 0,1008" fill="var(--green)"/>
    </svg>

    <h1 class="headline">
      <span class="kicker">A BEAUTIFUL</span>
      <span class="hero">GARDEN</span>
      <span class="tail">DOESN'T HAPPEN BY ITSELF</span>
    </h1>

    <div class="portrait" role="img" aria-label="Portrait photo of Doug Marlowe"></div>

    <div class="promo">
      <span class="line">SCHEDULE</span>
      <span class="line strong">APPOINTMENT</span>
      <span class="line call">JUST CALL US AT</span>
      <span class="phone">+123 987 6540</span>
    </div>

    <section class="welcome">
      <h2>WELCOME TO<br>MARLOWE GREENS</h2>
      <p>Marlowe Greens is your garden and lawn care specialist, with a passion for gardening and a keen eye for detail you can rest assured you're in the right hands.</p>
      <p>My services are tailored to meet every individual clients needs.<br>From a one time mow too regular lawn mowing, all aspects of garden care and even full garden makeovers.</p>
      <p>I go that extra mile every time to leave you garden and yard looking amazing. Free no obligation quotes, reliable and friendly service, great rates.</p>
    </section>

    <section class="profile">
      <h3>DOUG MARLOWE</h3>
      <p>From the beautiful Sunshine coast.<br>Doug has over 12 years of experience<br>in gardening and lawn care . With a<br>deep passion in Horticulture you<br>know your in the right hands.</p>
    </section>

    <section class="services core">
      <h3>GARDEN SERVICES</h3>
      <ul>
        <li>Lawn mowing</li>
        <li>Turf preparation and installation</li>
        <li>Tree and shrub pruning</li>
        <li>Eco friendly fertilizing</li>
        <li>Full garden makeovers</li>
        <li>Green waste removal</li>
        <li>Garden mulching</li>
        <li>Planting</li>
        <li>Hedging</li>
        <li>Weeding</li>
      </ul>
    </section>

    <section class="services extra">
      <h3>GARDEN SERVICES</h3>
      <ul>
        <li>Aluminium fencing and<br>gate installation and repairs</li>
        <li>Timber decking rejuvenation<br>and repairs</li>
        <li>Privacy screening</li>
        <li>Pressure cleaning</li>
        <li>And much more!</li>
      </ul>
    </section>

    <footer class="footer">
      <div class="brand"><span class="dot"></span>Marlowe Greens</div>
      <div class="divider"></div>
      <div class="contact">
        <h3>CONTACT US</h3>
        <div class="row">
          <svg width="10" height="13" viewBox="0 0 10 13"><path d="M5 0C2.2 0 0 2.2 0 5c0 3.6 5 8 5 8s5-4.4 5-8c0-2.8-2.2-5-5-5zm0 7a2 2 0 1 1 0-4 2 2 0 0 1 0 4z" fill="var(--green)"/></svg>
          <span>14 Kestrel Lane, Bramwood Heights 4572 Australia.</span>
        </div>
        <div class="row bottom">
          <div class="pair">
            <svg width="11" height="13" viewBox="0 0 11 13"><path d="M2.5 0.5l2 3-1.3 1.3c.6 1.6 1.8 3 3.3 3.8l1.3-1.2 2.7 2.2-1.2 2.4C5 11.6 0.8 6.8 0.5 2z" fill="var(--green)"/></svg>
            <span>0418 527 064</span>
          </div>
          <div class="pair">
            <svg width="14" height="14" viewBox="0 0 14 14"><circle cx="7" cy="7" r="6.2" fill="none" stroke="var(--green)" stroke-width="1.4"/><path d="M1 7h12M7 1c-3 3.5-3 8.5 0 12M7 1c3 3.5 3 8.5 0 12" fill="none" stroke="var(--green)" stroke-width="1.1"/></svg>
            <div class="web-lines">www.marlowegreens.com.au<br>doug@marlowegreens.com.au</div>
          </div>
        </div>
      </div>
    </footer>
  </article>
</div>
</body>
</html>
```